NOTE: I PROVIDED THE INCORRECT LOGO AND ONLY A HANDFUL OF PEOPLE NOTICED THAT IT WAS NOT THE ONE I DESCRIBED. THE LOGO I HAVE NOW ATTACHED MATCHES MY WEBSITE AND THE COLORS ON THE WEBSITE SHOULD BE USED FOR THE CARD.

PLEASE READ THE BUSINESS CARD DETAILS AND PROJECT MUST HAVES CAREFULLY.

I am looking for a business card that is powerful, a bit edgy, and although I work in the corporate world, not too formal. I would like to see designs that use the colors on my website www.brightmoorlane.com. I don't want the card to look washed out so please use shades of those colors that make them "pop". The "vibe" of the card needs to show substance and confidence while also reflecting that we're not your usual consultants.

The focus of my work is turning "people problems" into profits. Those problems could be poor service, an unstable workforce, untrained leaders, or managing change. We are an aggressive, results-focused team of performance improvement professionals who refuse to believe "things can't be done". For us, failure is not an option. Our logo reflects a target from the view of the site on a gun.

In addition to the contact information provided on the sample business card (do not include "turning people problems into profits"), I would like to include this statement (probably on the back):
I equip results-oriented business leaders to turn their people problems into profits in six months or less.

PLEASE NOTE THAT MY WEBSITE IS UNDER REVISION TO TONE DOWN THE MILITARY THEME, ALTHOUGH THE WARRIOR ENERGY AND FOCUS ON RESULTS REMAINS.

Target Market(s)

My clients are Mid and senior-level managers. I don't target any particular industry.

Industry/Entity Type

Consulting

Contact Information for Business Card

In addition to the contact information provided on the sample business card (DO NOT INCLUDE "turning people problems into profits"), I would like to include this statement (probably on the back):

I don't care whether the card is landscape or portrait view.

Font styles to use
Sans Serif

Requirements
Must have
• 1. be easy to read, no 6-8 point fonts!
• 2. a "vibe" that captures the eye without being too chaotic or busy
• 3. bold color, not washed out or boring - a good blend with the colors currently on my website (black, red, white, army green) but you don't need to use all of them.
• 4. all the contact information I have provided
• 5. a good blend with the colors currently on my website
• 6. Must have this quote on the back of the card: I equip results-oriented business leaders to turn their people problems into profits in six months or less.
Nice to have
• In looking at the sample images I provided for ideas, you can see that I like the way a card carries over from one side to the next.
• It would be great to find some aspect/quality/feature that I haven't seen before
Should not have
• 1. NO use of ALL CAPS
• 2. fonts that I would have to seek out and purchase (you should provide files for font if using something not standard)

```html
<!DOCTYPE html>
<html lang="en">
<head>
<meta charset="utf-8">
<title>Brightmoor Lane – Business Card</title>
<link rel="stylesheet" href="https://fonts.googleapis.com/css2?family=Open+Sans:wght@400&family=Signika:wght@600;700&family=Ubuntu:wght@400&display=swap">
<style>
  :root {
    --page: #ffffff;
    --card: #141414;
    --card-light: #1d1d1d;
    --ink: #ffffff;
    --red: #c4101c;
    --red-deep: #8e0d16;
    --army: #3c4d27;
    --label: #111111;
  }
  * { margin: 0; padding: 0; box-sizing: border-box; }
  html, body { width: 934px; height: 1200px; overflow: hidden; background: var(--page); }
  .sheet { position: relative; width: 934px; height: 1200px; font-family: "Ubuntu", sans-serif; color: var(--ink); }

  .side-label {
    position: absolute; left: 0; width: 934px; text-align: center;
    font-family: "Open Sans", sans-serif; font-size: 33px; color: var(--label); line-height: 1;
  }
  .side-label--front { top: 20px; }
  .side-label--back { top: 626px; }

  .card {
    position: absolute; left: 0; width: 934px;
    background: radial-gradient(ellipse at 40% 40%, var(--card-light), var(--card) 70%);
  }
  .card--front { top: 63px; height: 534px; }
  .card--back { top: 665px; height: 535px; }

  .card > * { position: absolute; }

  .brand-dot { border-radius: 50%; background: var(--ink); }
  .brand-name { font-family: "Signika", sans-serif; font-weight: 700; color: var(--ink); line-height: 1; white-space: nowrap; }
  .brand-rule { height: 1px; background: rgba(255,255,255,0.55); }

  .card--front .brand-dot { left: 78px; top: 78px; width: 140px; height: 140px; }
  .card--front .brand-name--top { left: 229px; top: 95px; font-size: 58px; }
  .card--front .brand-rule { left: 229px; top: 166px; width: 294px; }
  .card--front .brand-name--bottom { left: 229px; top: 186px; font-size: 62px; }

  .person-name {
    left: 211px; top: 258px; font-family: "Signika", sans-serif; font-weight: 600;
    font-size: 50px; color: var(--red); line-height: 1; white-space: nowrap;
  }
  .person-title {
    left: 247px; top: 308px; font-family: "Signika", sans-serif; font-weight: 600;
    font-size: 38px; color: var(--army); line-height: 1; white-space: nowrap;
  }
  .title-rule { left: 249px; top: 348px; width: 512px; height: 2px; background: var(--red); }

  .contact { font-size: 32px; line-height: 44px; white-space: nowrap; }
  .contact--phones { left: 71px; top: 380px; }
  .contact--web { right: 69px; top: 380px; text-align: right; }

  .ornament { border-radius: 50%; background: var(--red-deep); opacity: 0.55; }
  .ornament--front { left: 428px; top: 406px; width: 44px; height: 44px; }
  .ornament--back-top { left: 765px; top: 79px; width: 90px; height: 90px; }
  .ornament--back-bottom { left: 74px; top: 367px; width: 90px; height: 90px; }

  .statement {
    left: 71px; top: 60px; width: 690px; font-size: 41px; line-height: 58px;
  }

  .card--back .brand-dot { left: 422px; top: 332px; width: 100px; height: 100px; }
  .card--back .brand-name--top { left: 533px; top: 335px; font-size: 50px; }
  .card--back .brand-rule { left: 533px; top: 392px; width: 218px; }
  .card--back .brand-name--bottom { left: 533px; top: 403px; font-size: 52px; }
</style>
</head>
<body>
<main class="sheet">
  <p class="side-label side-label--front">Front</p>

  <section class="card card--front">
    <div class="brand-dot"></div>
    <p class="brand-name brand-name--top">Brightmoor</p>
    <div class="brand-rule"></div>
    <p class="brand-name brand-name--bottom">Lane</p>

    <p class="person-name">Dana Whitfield</p>
    <p class="person-title">Chief Performance Strategist</p>
    <div class="title-rule"></div>

    <p class="contact contact--phones">Work: 555.014.2270<br>Cell: 555.019.4831</p>
    <div class="ornament ornament--front" role="img" aria-label="Small red target reticle ornament"></div>
    <p class="contact contact--web">dana@brightmoorlane.com<br>www.brightmoorlane.com</p>
  </section>

  <p class="side-label side-label--back">Back</p>

  <section class="card card--back">
    <p class="statement">I equip results-oriented business leaders to turn their people problems into profits in six months or less.</p>
    <div class="ornament ornament--back-top" role="img" aria-label="Red target reticle ornament"></div>
    <div class="ornament ornament--back-bottom" role="img" aria-label="Red target reticle ornament"></div>

    <div class="brand-dot"></div>
    <p class="brand-name brand-name--top">Brightmoor</p>
    <div class="brand-rule"></div>
    <p class="brand-name brand-name--bottom">Lane</p>
  </section>
</main>
</body>
</html>
```